Flier Template in Microsoft Word

We need to a have a flier about farm practices developed in Microsoft Word. Each farm will able to add their own logos and photos. We will give them a model that they can customize.

We want a traditional "country" flavor. Green colors and earth tones are best. Please use the photos we have provided.

The final product must be in Microsoft Word for our farmers to customize.
Updates

All designers: Please have a white background (maybe with a watermark). Our client will print these on white paper using a desktop printer. Thank you!

Target Market(s)

People who shop at Farmer's Markets, join CSAs, and enjoy cooking with fresh vegetables.

Industry/Entity Type

Farm

Font styles to use
Serif

Requirements
Must have
• Must use the text and general layout of the Microsoft Word document attached
Must use the pictures we provided.
Final product must be in Microsoft Word
Must be able to easily swap out the logo at the top
Must be able to print on white paper on a desktop printer
Nice to have
• A nice header that looks like a farm or food on the table
A nice watermark or background to make the flier look polished
Should not have
• Do not change the photos
Do not use high tech fonts or graphic treatments

```html
<!DOCTYPE html>
<html lang="en">
<head>
<meta charset="utf-8">
<title>Sustainable Grazing Flier</title>
<link rel="stylesheet" href="https://fonts.googleapis.com/css2?family=Questrial&family=Carlito:wght@400;700&display=swap">
<style>
  :root {
    --backdrop: #ecebe7;
    --paper: #ffffff;
    --band: #1f1d18;
    --ink: #222222;
    --body-ink: #3a3a3a;
    --olive: #56591f;
    --rule: #2b2b2b;
    --sky: #9fbfd9;
    --meadow: #6f8f3e;
    --earth: #8a6f4a;
    --produce: #b5532e;
    --kitchen: #d9b98a;
    --water: #5c7f8f;
    --dusk: #7a5a35;
  }
  * { margin: 0; padding: 0; box-sizing: border-box; }
  html, body { width: 1200px; height: 831px; overflow: hidden; }
  body { background: var(--backdrop); font-family: "Carlito", "Calibri", sans-serif; color: var(--body-ink); position: relative; }

  .page { position: absolute; top: 43px; width: 537px; height: 761px; background: var(--paper); }
  .page--front { left: 35px; }
  .page--back { left: 627px; }
  .page__band { position: absolute; left: 0; right: 0; background: var(--band); }
  .page__band--top { top: 0; height: 23px; }
  .page__band--bottom { bottom: 0; height: 28px; }

  .abs { position: absolute; }
  .photo { position: absolute; }

  .logo-slot { left: 21px; top: 60px; font-family: "Questrial", sans-serif; font-size: 21px; color: var(--ink); letter-spacing: 0.5px; }
  .header-photo { left: 174px; top: 23px; width: 363px; height: 70px; background: linear-gradient(180deg, var(--sky) 0%, #cfe0ea 40%, #5f8a3a 62%, #4a6b2c 100%); }

  .title { left: 0; width: 537px; top: 100px; text-align: center; font-family: "Questrial", sans-serif; font-weight: 700; font-size: 18px; color: var(--ink); letter-spacing: 0.4px; }
  .subtitle { left: 0; width: 537px; top: 128px; text-align: center; font-family: "Carlito", sans-serif; font-weight: 700; font-size: 13.5px; color: var(--olive); }

  .section-heading { font-family: "Questrial", sans-serif; font-size: 15px; color: var(--ink); letter-spacing: 0.3px; }
  .body-copy { font-size: 10px; line-height: 13.8px; color: var(--body-ink); }

  .who-heading { left: 48px; top: 167px; }
  .who-copy { left: 48px; top: 186px; width: 240px; }
  .farmer-photo { left: 301px; top: 153px; width: 184px; height: 129px; background: linear-gradient(180deg, #b9cfdc 0%, #8fa7a0 35%, #5e8b3a 60%, #4c7430 100%); }

  .done-heading { left: 48px; top: 278px; }
  .done-copy { left: 48px; top: 296px; width: 445px; }

  .when-heading { left: 48px; top: 376px; }
  .when-copy { left: 48px; top: 395px; width: 445px; }

  .before-photo { left: 48px; top: 469px; width: 213px; height: 148px; background: linear-gradient(180deg, #a9c1d8 0%, #8a9b8c 35%, #6f7a4f 60%, var(--earth) 100%); }
  .after-photo { left: 276px; top: 469px; width: 211px; height: 148px; background: linear-gradient(180deg, #aec8de 0%, #8fa592 35%, #6c8f3c 60%, #587a2e 100%); }
  .photo-label { top: 629px; width: 120px; text-align: center; font-family: "Questrial", sans-serif; font-weight: 700; font-size: 13.5px; color: var(--ink); }
  .before-label { left: 83px; }
  .after-label { left: 328px; }

  .partner { position: absolute; left: 48px; top: 672px; width: 78px; display: flex; align-items: center; gap: 4px; font-size: 11px; color: var(--olive); font-family: "Carlito", sans-serif; }
  .partner__dot { width: 14px; height: 14px; border-radius: 50%; background: var(--olive); flex: none; }
  .partner-copy { left: 135px; top: 682px; width: 360px; font-size: 10px; line-height: 14.5px; color: var(--ink); }

  .care-heading { left: 51px; top: 49px; }
  .care-copy { left: 51px; top: 76px; width: 445px; }

  .grid-rule { position: absolute; background: var(--rule); }
  .grid-rule--v { left: 268px; top: 157px; width: 1.5px; height: 489px; }
  .grid-rule--h { left: 48px; top: 396px; width: 442px; height: 1.5px; }

  .market-photo { left: 51px; top: 171px; width: 200px; height: 141px; background: linear-gradient(135deg, var(--produce) 0%, #c98a3d 45%, #7d8c4a 100%); }
  .kitchen-photo { left: 287px; top: 171px; width: 201px; height: 141px; background: linear-gradient(135deg, #f1ece4 0%, var(--kitchen) 55%, #b74a2a 100%); }
  .fishing-photo { left: 51px; top: 424px; width: 201px; height: 141px; background: linear-gradient(180deg, #b8cfdc 0%, var(--water) 50%, #4e5a3c 100%); }
  .osprey-photo { left: 288px; top: 424px; width: 201px; height: 141px; background: linear-gradient(135deg, #c79a5c 0%, var(--dusk) 55%, #3d2c18 100%); }

  .caption { text-align: center; font-size: 10.5px; line-height: 15.5px; color: var(--ink); }
  .caption--market { left: 58px; top: 327px; width: 190px; }
  .caption--kitchen { left: 288px; top: 327px; width: 200px; }
  .caption--streams { left: 58px; top: 585px; width: 190px; }
  .caption--wildlife { left: 290px; top: 587px; width: 196px; }
</style>
</head>
<body>

<section class="page page--front">
  <div class="page__band page__band--top"></div>

  <div class="abs logo-slot">YOUR LOGO</div>
  <div class="photo header-photo" role="img" aria-label="Farm landscape with a white barn, trees and green pasture"></div>

  <h1 class="abs title">SUSTAINABLE GRAZING</h1>
  <p class="abs subtitle">Happier Cows = Healthier Milk and Cleaner Streams</p>

  <h2 class="abs section-heading who-heading">WHO WE ARE</h2>
  <p class="abs body-copy who-copy">Hollow Creek Dairy Farm is a third generation dairy farm located on 64 acres in the Linden Valley. We raise Holsteins to produce milk and also raise hens for eggs. We sell much of our milk, as well as cheese, yogurt and baked goods directly from the farm.</p>
  <div class="photo farmer-photo" role="img" aria-label="Farmer standing in front of a red tractor in a green field"></div>

  <h2 class="abs section-heading done-heading">WHAT HAVE WE DONE</h2>
  <p class="abs body-copy done-copy">At Hollow Creek Dairy Farm, we take care of our animals and our animals help us take care of the land. Corn and other grains are not a natural part of a cows' diet, so we don't feed them that. Instead, we let them roam the pastures eating grass and other plants. We move the cows from pasture to pasture on a thoughtful schedule to prevent overgrazing, and this reduces soil erosion and water pollution. Our animals are happier and our land and water is healthier.</p>

  <h2 class="abs section-heading when-heading">WHEN AND WHERE WE DID IT</h2>
  <p class="abs body-copy when-copy">In 2010, we had our cows in a stall barn and corn or soybeans in our fields. We looked into switching some of our acreage from crops to pasture and soon realized that it would beneficial to our cows and our soil. We then installed fencing to divide the fields into smaller paddocks and in spring 2011, we planted a seed mixture containing plants that provide the nutrition our cows need and that provides support for the soil.</p>

  <div class="photo before-photo" role="img" aria-label="Before: cattle grazing beside an eroded stream bank"></div>
  <div class="photo after-photo" role="img" aria-label="After: fenced, green stream bank with restored vegetation"></div>
  <p class="abs photo-label before-label">BEFORE</p>
  <p class="abs photo-label after-label">AFTER</p>

  <div class="partner"><span class="partner__dot"></span><span>Ridgeline</span></div>
  <p class="abs partner-copy">Ridgeline Council's growing promotes local farms that produce fresh, high quality, healthy environmental farm practices that keep our water clean and our families safe.</p>

  <div class="page__band page__band--bottom"></div>
</section>

<section class="page page--back">
  <div class="page__band page__band--top"></div>

  <h2 class="abs section-heading care-heading">WHY YOU SHOULD CARE</h2>
  <p class="abs body-copy care-copy">Hollow Creek Dairy Farm is a third generation dairy farm located on 64 acres in the Linden Valley. We raise Holsteins to produce milk and also raise hens for eggs. We sell much of our milk, as well as cheese, yogurt and baked goods directly from the farm.</p>

  <div class="grid-rule grid-rule--v"></div>
  <div class="grid-rule grid-rule--h"></div>

  <div class="photo market-photo" role="img" aria-label="Farmers market stall with apples and fresh produce"></div>
  <div class="photo kitchen-photo" role="img" aria-label="Parent and child preparing fresh vegetables in a kitchen"></div>
  <p class="abs caption caption--market">Fresh and locally produced food from our farm tastes better, and it's better for our local economy and environment.</p>
  <p class="abs caption caption--kitchen">Fresh food is healthier for kids of all ages than processed food.</p>

  <div class="photo fishing-photo" role="img" aria-label="Family holding a fish caught in a clean river"></div>
  <div class="photo osprey-photo" role="img" aria-label="Osprey lifting off from the water"></div>
  <p class="abs caption caption--streams">As a result of the improvements described here, the waterways that run through our farm are cleaner, benefitting everyone downstream.</p>
  <p class="abs caption caption--wildlife">Our wildlife neighbours appreciate the cleaner waterways even more than you do!</p>

  <div class="partner"><span class="partner__dot"></span><span>Ridgeline</span></div>
  <p class="abs partner-copy">Ridgeline Council's growing promotes local farms that produce fresh, high quality, healthy environmental farm practices that keep our water clean and our families safe.</p>

  <div class="page__band page__band--bottom"></div>
</section>

</body>
</html>
```